TJ&R Roofing Billboard Design

Looking for a fresh new billboard design with my new headshot photo and using some info from my previous billboard and maybe website for design/content inspiration. My website is https://tjrroofing-example.com/

Also attached are my logo and current lawn sign design. I am looking for something simple, clean and modern. The landing page website should be 3182roof-example.com like my previous billboard has.

```html
<!DOCTYPE html>
<html lang="en">
<head>
<meta charset="UTF-8">
<title>TJ&amp;R Roofing Billboard</title>
<link rel="stylesheet" href="https://fonts.googleapis.com/css2?family=Archivo+Black&family=League+Spartan:wght@500;600&family=Alegreya:wght@400&display=swap">
<style>
  :root {
    --navy: #22375e;
    --navy-deep: #1b2d4f;
    --olive: #8a9d2c;
    --olive-band: #8fa33a;
    --white: #ffffff;
    --page: #e9edf2;
    --photo-warm: #8a6a5e;
    --photo-shirt: #c3cfe0;
    --shingle: #5d6a7c;
  }
  * { margin: 0; padding: 0; box-sizing: border-box; }
  html, body {
    width: 1200px; height: 800px; overflow: hidden;
    background: var(--page);
  }
  .billboard {
    position: absolute; left: 20px; top: 225px;
    width: 1160px; height: 349px;
    background: var(--navy);
    overflow: hidden;
  }
  .shingle-photo {
    position: absolute; right: 0; top: 0;
    width: 300px; height: 280px;
    background: linear-gradient(100deg, rgba(34,55,94,1) 0%, rgba(34,55,94,0.6) 35%, var(--shingle) 75%, #7c8796 100%);
  }
  .green-band { position: absolute; left: 0; top: 0; width: 1160px; height: 349px; }
  .headshot-photo {
    position: absolute; left: 0; top: 0;
    width: 340px; height: 349px;
    background:
      linear-gradient(180deg, rgba(27,45,79,0) 0%, rgba(27,45,79,0) 55%, var(--photo-shirt) 80%, var(--photo-shirt) 100%),
      linear-gradient(90deg, var(--navy-deep) 0%, var(--photo-warm) 45%, var(--navy) 100%);
    -webkit-mask-image: linear-gradient(90deg, #000 80%, transparent 100%);
            mask-image: linear-gradient(90deg, #000 80%, transparent 100%);
  }
  .brand {
    position: absolute; left: 274px; top: 58px; width: 240px;
    text-align: center; color: var(--white);
  }
  .brand-mark {
    display: block; width: 42px; height: 42px; border-radius: 50%;
    background: var(--white); margin: 0 auto 12px;
  }
  .brand-name {
    font-family: "League Spartan", sans-serif; font-weight: 500;
    font-size: 24px; white-space: nowrap; letter-spacing: 0.3px;
  }
  .brand-tagline {
    font-family: "Alegreya", serif; font-size: 19px;
    white-space: nowrap; margin-top: 24px;
  }
  .headline {
    position: absolute; left: 548px; top: 40px; width: 440px;
    font-family: "Archivo Black", sans-serif; color: var(--olive);
    line-height: 0.92; text-transform: uppercase; white-space: nowrap;
  }
  .headline-top { display: block; font-size: 70px; letter-spacing: -0.5px; }
  .headline-bottom { display: block; font-size: 53px; letter-spacing: -0.5px; }
  .price-box {
    position: absolute; left: 549px; top: 165px;
    width: 432px; height: 71px; background: var(--white);
    display: flex; align-items: center; justify-content: center;
    font-family: "Archivo Black", sans-serif; font-size: 34px;
    color: var(--navy); text-transform: uppercase; letter-spacing: -0.3px;
    white-space: nowrap;
  }
  .landing-url {
    position: absolute; left: 450px; top: 295px;
    font-family: "League Spartan", sans-serif; font-weight: 500;
    font-size: 28px; color: var(--white); white-space: nowrap;
  }
  .call-to-action {
    position: absolute; right: 31px; top: 293px;
    font-family: "Archivo Black", sans-serif; font-size: 32px;
    color: var(--white); text-transform: uppercase; letter-spacing: -0.3px;
    white-space: nowrap;
  }
</style>
</head>
<body>
  <div class="billboard">
    <div class="shingle-photo" role="img" aria-label="Close-up photo of dark asphalt roof shingles"></div>
    <svg class="green-band" viewBox="0 0 1160 349" aria-hidden="true">
      <path d="M300 349 C330 300 350 282 400 280 Q760 272 1160 245 L1160 349 Z" fill="var(--olive-band)"/>
    </svg>
    <div class="headshot-photo" role="img" aria-label="Headshot photo of the company owner smiling, in a light blue shirt"></div>
    <div class="brand">
      <span class="brand-mark"></span>
      <div class="brand-name">TJ&amp;R Roofing LLC</div>
      <div class="brand-tagline">Built Strong, Built to Last</div>
    </div>
    <h1 class="headline">
      <span class="headline-top">Full Roof</span>
      <span class="headline-bottom">Replacement</span>
    </h1>
    <div class="price-box">Starting at $7,499</div>
    <div class="landing-url">3182roof-example.com</div>
    <div class="call-to-action">Get a Free Quote</div>
  </div>
</body>
</html>
```